Create a beautiful brochure for a Permanent Make Up Clinic

I need a classy brochure for my Permanent Make up Clinic. It needs a classy cover and the list of services and extra information on the inside. I don't have any requirements on size of the brochure, but it needs to look attractive and upmarket. The colors I like are black -white - Gold - grey. I like a minimalistic look.
I’d like to have my logo on the cover, the price list on the inside and the address information at the back.

Target Market(s)

woman between 18 and 99 years old

Industry/Entity Type

Beauty

Font styles to use
Sans Serif
Script

Colors

Designer to choose colors to be used in the design.

Requirements
Must have
• the logo on the cover
• pictures of the services with an explanation and pricing
• address information at the back
Nice to have
• a classy upmarket look, not with too many different colors in it.

```html
<!DOCTYPE html>
<html lang="nl">
<head>
<meta charset="utf-8">
<title>Velora Clinic – Brochure</title>
<link rel="stylesheet" href="https://fonts.googleapis.com/css2?family=Montserrat:wght@300;400;500;600;700;800&family=Raleway:wght@200;300;400&display=swap">
<style>
:root{
  --gold:#c9a253;
  --gold-light:#e8cf8e;
  --gold-dark:#8a6a2c;
  --navy:#1d2533;
  --slate:#3a4658;
  --grey:#6d747e;
  --grey-light:#e9eaec;
  --ink:#2a2d33;
  --paper:#ffffff;
  --canvas:#f2f2f2;
}
*{box-sizing:border-box;margin:0;padding:0}
html,body{width:779px;height:1200px;overflow:hidden;background:var(--canvas)}
body{position:relative;font-family:'Montserrat',sans-serif;color:var(--ink)}
.spread{position:absolute;left:20px;width:739px;display:flex;box-shadow:0 2px 8px rgba(0,0,0,.18)}
.spread--outer{top:15px;height:545px}
.spread--inner{top:625px;height:560px}
.page{position:relative;width:50%;height:100%;overflow:hidden;background:var(--paper)}
.photo{position:absolute;border-radius:50%}
.ring{position:absolute;border-radius:50%;border:3px solid var(--gold)}
.brand{font-family:'Raleway',sans-serif;font-weight:300;letter-spacing:2px;text-align:center}
.small{font-size:6.4px;line-height:1.55;color:var(--grey)}

/* back page */
.back__hero{left:-30px;top:-20px;width:250px;height:250px;background:radial-gradient(circle at 55% 45%,#e4c3ad,#a9826b 60%,#5a4236)}
.back__portrait{left:50px;top:252px;width:110px;height:110px;background:radial-gradient(circle at 50% 40%,#f0d8c8,#b88f76 60%,#6b4c3c)}
.back__portrait-ring{left:44px;top:246px;width:122px;height:122px}
.back__intro{position:absolute;left:230px;top:165px;width:125px}
.back__intro p{margin-bottom:6px}
.back__social{position:absolute;left:28px;top:255px;width:0}
.back__logo{position:absolute;left:0;right:0;top:370px}
.back__logo .brand{font-size:28px;color:var(--ink)}
.back__logo .tag{font-size:5px;letter-spacing:1.5px;color:var(--grey);text-align:center;margin-top:4px;text-transform:uppercase}
.back__contact{position:absolute;left:22px;right:22px;top:455px;display:flex;justify-content:space-between}
.back__contact h3{font-size:8px;font-weight:700;letter-spacing:.5px;margin-bottom:8px}
.contact-row{display:flex;align-items:center;gap:5px;font-size:6px;color:var(--grey);margin-bottom:5px}
.contact-row svg{width:9px;height:9px;flex:none}
.back__bar{position:absolute;left:22px;right:22px;bottom:14px;border-top:1px solid var(--grey-light);padding-top:6px;display:flex;gap:14px;font-size:5.5px;color:var(--grey)}

/* cover */
.cover{background:linear-gradient(160deg,#2c3646 0%,var(--navy) 55%,#10151e 100%)}
.cover__logo{position:absolute;left:0;right:0;top:20px}
.cover__logo .brand{font-size:26px;color:#fff}
.cover__logo .tag{font-size:5px;letter-spacing:1.5px;color:#c8ccd3;text-align:center;margin-top:3px;text-transform:uppercase}
.cover__swoosh{position:absolute;left:0;top:0}
.cover__photo{left:110px;top:125px;width:250px;height:250px;background:radial-gradient(circle at 45% 50%,#d9b7a2,#9a7766 55%,#3c3b44)}
.cover__ring{left:104px;top:119px;width:262px;height:262px}
.cover__headline{position:absolute;right:22px;top:430px;text-align:right;color:#fff;font-weight:800;font-size:17px;line-height:1.2;letter-spacing:.3px}
.cover__rule{position:absolute;right:22px;top:478px;width:150px;height:2px;background:var(--gold)}
.cover__web{position:absolute;right:22px;bottom:18px;font-size:6px;letter-spacing:1.5px;color:#c8ccd3}

/* inside left */
.inside-left__wave{position:absolute;left:0;top:0}
.inside-left__photo{left:22px;top:45px;width:120px;height:120px;background:radial-gradient(circle at 50% 45%,#eacdb8,#b68c73 60%,#5f4436)}
.inside-left__ring{left:16px;top:39px;width:132px;height:132px}
.inside-left__body{position:absolute;left:22px;right:26px;top:190px}
.inside-left__body p{font-size:6.6px;line-height:1.6;color:var(--ink);margin-bottom:8px}
.lead-gold{font-size:8px!important;font-weight:600;color:var(--gold)!important;line-height:1.3!important;margin-bottom:10px!important}
.ticks{list-style:none;margin-bottom:14px}
.ticks li{position:relative;padding-left:12px;font-size:6.6px;line-height:1.55;margin-bottom:7px}
.ticks li::before{content:"";position:absolute;left:0;top:3px;width:5px;height:5px;background:var(--gold)}
.inside-left__foot{position:absolute;left:0;bottom:0}

/* inside right */
.services__title{position:absolute;left:22px;top:30px;width:200px;font-size:13px;font-weight:700;line-height:1.25;color:var(--ink)}
.services__lips{left:245px;top:12px;width:105px;height:105px;background:radial-gradient(ellipse at 50% 55%,#c98a86,#a46a67 45%,#e6cfc4 75%)}
.services__lips-ring{left:240px;top:7px;width:115px;height:115px}
.service-list{position:absolute;left:22px;right:22px;top:110px;list-style:none}
.service-list li{position:relative;padding-left:12px;margin-bottom:9px}
.service-list li::before{content:"";position:absolute;left:0;top:3px;width:6px;height:6px;background:var(--gold)}
.service-list h4{font-size:7.5px;font-weight:700;color:var(--ink)}
.service-list h4 span{color:var(--gold)}
.service-list p{font-size:6px;line-height:1.5;color:var(--grey);margin-top:2px}
.consult__title{position:absolute;left:22px;top:395px;font-size:13px;font-weight:700;letter-spacing:.5px}
.consult__title span{font-weight:400;font-size:9px;color:var(--grey)}
.consult__row{position:absolute;left:22px;right:22px;display:flex;gap:12px}
.consult__img{width:70px;height:52px;flex:none}
.consult__img--a{background:linear-gradient(135deg,#d8c3b5,#9d8272)}
.consult__img--b{background:linear-gradient(135deg,#cfc9c4,#7e746e)}
.consult__row p{font-size:6px;line-height:1.55;color:var(--grey)}
</style>
</head>
<body>

<section class="spread spread--outer">
  <article class="page back">
    <div class="photo back__hero" role="img" aria-label="Close-up photo of a brow treatment being applied"></div>
    <div class="photo back__portrait" role="img" aria-label="Portrait photo of the clinic's specialist"></div>
    <div class="ring back__portrait-ring"></div>

    <div class="back__intro">
      <p class="small">Bij Velora Clinic werken we met zorgvuldig gekozen technieken en pigmenten, afgestemd op uw huid en gezichtsvorm.</p>
      <p class="small">Elke behandeling begint met een persoonlijk gesprek, zodat het resultaat natuurlijk oogt en bij u past.</p>
    </div>

    <div class="back__logo">
      <div class="brand">velora</div>
      <div class="tag">Permanente make-up &amp; medische tatoeage</div>
    </div>

    <div class="back__contact">
      <div>
        <h3>HEB JE NOG VRAGEN?</h3>
        <div class="contact-row">
          <svg viewBox="0 0 10 10"><path d="M2 1h2l1 2.5-1.2.8a5 5 0 0 0 2 2l.8-1.2L9 6v2a1 1 0 0 1-1 1A7 7 0 0 1 1 2a1 1 0 0 1 1-1z" fill="#c9a253"/></svg>
          +31 (0)20 555 0142
        </div>
        <div class="contact-row">
          <svg viewBox="0 0 10 10"><rect x="1" y="2" width="8" height="6" fill="none" stroke="#c9a253"/><path d="M1 2l4 3.5L9 2" fill="none" stroke="#c9a253"/></svg>
          info@veloraclinic.nl
        </div>
      </div>
      <div>
        <h3>EMAIL OF WEBWINKEL</h3>
        <div class="contact-row">
          <svg viewBox="0 0 10 10"><path d="M5 9.5S1.8 6 1.8 4a3.2 3.2 0 0 1 6.4 0C8.2 6 5 9.5 5 9.5z" fill="#c9a253"/><circle cx="5" cy="4" r="1.1" fill="#fff"/></svg>
          Lindelaan 24
        </div>
        <div class="contact-row" style="padding-left:14px">1071 AB Amsterdam</div>
        <div class="contact-row">
          <svg viewBox="0 0 10 10"><circle cx="5" cy="5" r="4" fill="none" stroke="#c9a253"/><path d="M1 5h8M5 1c-2 2.5-2 5.5 0 8M5 1c2 2.5 2 5.5 0 8" fill="none" stroke="#c9a253" stroke-width=".7"/></svg>
          www.veloraclinic.nl
        </div>
      </div>
    </div>
    <div class="back__bar"><span>■ @veloraclinic</span><span>■ veloraclinic</span></div>
  </article>

  <article class="page cover">
    <svg class="cover__swoosh" width="370" height="545" viewBox="0 0 370 545">
      <defs>
        <linearGradient id="coverGold" x1="0" y1="0" x2="1" y2="1">
          <stop offset="0" stop-color="#8a6a2c"/><stop offset=".5" stop-color="#e8cf8e"/><stop offset="1" stop-color="#8a6a2c"/>
        </linearGradient>
      </defs>
      <path d="M0 250 C60 110 190 60 370 95 L370 112 C200 80 80 130 0 280Z" fill="url(#coverGold)" opacity=".9"/>
      <path d="M0 545 L0 440 C90 470 220 420 370 330 L370 545Z" fill="#0d1119" opacity=".55"/>
    </svg>
    <div class="cover__logo">
      <div class="brand">velora</div>
      <div class="tag">Permanente make-up &amp; medische tatoeage</div>
    </div>
    <div class="photo cover__photo" role="img" aria-label="Photo of a woman receiving a permanent make-up treatment"></div>
    <div class="ring cover__ring"></div>
    <h1 class="cover__headline">BENADRUK JE<br>NATUURLIJKE SCHOONHEID!</h1>
    <div class="cover__rule"></div>
    <div class="cover__web">www.veloraclinic.nl</div>
  </article>
</section>

<section class="spread spread--inner">
  <article class="page inside-left">
    <svg class="inside-left__wave" width="370" height="150" viewBox="0 0 370 150">
      <defs>
        <linearGradient id="waveGold" x1="0" y1="0" x2="1" y2="0">
          <stop offset="0" stop-color="#2a2d33"/><stop offset=".55" stop-color="#8a6a2c"/><stop offset="1" stop-color="#e8cf8e"/>
        </linearGradient>
      </defs>
      <path d="M0 0H370V40C280 95 200 70 120 110 80 130 40 120 0 140Z" fill="url(#waveGold)"/>
      <path d="M150 112C230 70 300 95 370 52V62C300 105 235 82 160 118Z" fill="#e8cf8e"/>
    </svg>
    <div class="photo inside-left__photo" role="img" aria-label="Portrait photo of a woman with defined brows"></div>
    <div class="ring inside-left__ring"></div>

    <div class="inside-left__body">
      <p>Permanent make-up, de behandeling die alle kleur waard is. Wij pigmenteren met uiterste precisie en nemen de tijd om uw wensen goed te begrijpen, zodat u dagelijks tijd bespaart en zich zelfverzekerd voelt.</p>
      <p class="lead-gold">Velora Clinic garandeert zorgvuldig werk en een persoonlijke aanpak tijdens elke behandeling</p>
      <ul class="ticks">
        <li>Wij werken met gecertificeerde pigmenten die veilig en huidvriendelijk zijn.</li>
        <li>Elke behandeling wordt vooraf ingetekend en pas na uw akkoord uitgevoerd.</li>
        <li>Een nabehandeling na zes weken is altijd bij de prijs inbegrepen.</li>
        <li>U ontvangt na afloop een verzorgingsset en duidelijke adviezen voor thuis.</li>
      </ul>
      <p>Wilt u meer weten over de mogelijkheden? Neem gerust contact op voor een vrijblijvend adviesgesprek. Samen bekijken we welke techniek het beste aansluit bij uw wensen.</p>
    </div>
    <svg class="inside-left__foot" width="370" height="80" viewBox="0 0 370 80">
      <path d="M0 80V30C110 70 250 0 370 40V80Z" fill="#e9eaec"/>
      <path d="M0 80V55C130 80 260 40 370 65V80Z" fill="#3a4658"/>
    </svg>
  </article>

  <article class="page services">
    <h2 class="services__title">We bekijken samen de meest geschikte techniek voor u:</h2>
    <div class="photo services__lips" role="img" aria-label="Close-up photo of lips with permanent lip colour"></div>
    <div class="ring services__lips-ring"></div>

    <ul class="service-list">
      <li><h4>Powder Brows Magic Shading techniek: <span>€ 350</span></h4><p>Zachte, gepoederde wenkbrauwen met een natuurlijke schaduw die tot twee jaar mooi blijft.</p></li>
      <li><h4>Full Lips Aquarelle Techniek: <span>€ 395</span></h4><p>Lippen krijgen een frisse kleur en een mooi gedefinieerde contour voor een vollere uitstraling.</p></li>
      <li><h4>Klassieke eyeliner: <span>€ 250</span></h4><p>Een subtiele lijn langs de wimpers die uw ogen de hele dag accentueert.</p></li>
      <li><h4>Soft eyeliner: <span>€ 275</span></h4><p>Een zacht uitlopende lijn voor een natuurlijk resultaat zonder harde randen.</p></li>
      <li><h4>Eyeliner onder het oog: <span>€ 150</span></h4><p>Een aanvulling op de bovenlijn voor extra diepte en expressie.</p></li>
    </ul>

    <h3 class="consult__title">GRATIS <span>ADVIESGESPREK</span></h3>
    <div class="consult__row" style="top:425px">
      <div class="consult__img consult__img--a" role="img" aria-label="Photo of a consultation at the clinic"></div>
      <p>Tijdens het gratis adviesgesprek bespreken we uw wensen, bekijken we uw huid en tekenen we de vorm alvast voor. Zo weet u precies wat u kunt verwachten.</p>
    </div>
    <div class="consult__row" style="top:487px">
      <div class="consult__img consult__img--b" role="img" aria-label="Photo of the treatment room"></div>
      <p>U kunt ook telefonisch een afspraak maken. Wij nemen ruim de tijd voor al uw vragen, zonder enige verplichting.</p>
    </div>
  </article>
</section>

</body>
</html>
```